Website for healthcare regulator

Responsive website development for a local association.

Design has already been completed with details below and in the uploaded files. This design must be followed closely.

Designer must provide full implementation/coding in WordPress.

Responsive website development for a local physician licensing organization. The Board for Medical Practice of Greyhaven and Tollmere regulates the practice of medicine in the public interest.

Development is required for the following pages based on the provided design:
1. Front Page (Desktop)
2. Front Page (Mobile)
3. Interior Page (Desktop)
4. Interior Page (Mobile)

The site will eventually integrate a physician search and login using a third party app called IMIS. An example of this can be seen in the current BMPGT website (bmpgt-site .ca).

Site must be responsive up to 1920px wide and down to mobile devices (~360px). Please don’t include site builder plugin or themes (such as muffin builder or visual composer). Please use sidebars and widgets.

Reference files can be found within this brief.

```html
<!DOCTYPE html>
<html lang="en">
<head>
<meta charset="utf-8">
<title>BMPGT – Board for Medical Practice of Greyhaven and Tollmere</title>
<link href="https://fonts.googleapis.com/css2?family=Poppins:wght@400;500;600;700;800&display=swap" rel="stylesheet">
<style>
:root{
  --navy:#0b1f4d;
  --blue:#0a2f8c;
  --gold:#7a4a12;
  --ink:#111;
  --text:#333;
  --muted:#666;
  --grey:#f2f2f2;
  --white:#fff;
  --line:#ddd;
}
*{box-sizing:border-box;margin:0;padding:0}
html,body{width:1200px;height:3040px;overflow:hidden}
body{font-family:'Poppins',sans-serif;color:var(--text);background:var(--white);position:relative}
a{color:inherit;text-decoration:none}

/* header */
.site-header{position:absolute;top:0;left:0;width:1200px;height:77px;background:var(--white)}
.brand{position:absolute;left:24px;top:24px;font-weight:600;font-size:22px;line-height:30px;color:var(--navy)}
.main-nav{position:absolute;left:540px;top:28px;display:flex;align-items:center;font-size:12.5px;font-weight:500;color:var(--ink)}
.main-nav .search-ico{margin-right:16px}
.main-nav .sep{width:1px;height:14px;background:var(--line);margin-right:18px}
.main-nav a{margin-right:26px}
.main-nav .caret{font-size:8px;margin-left:3px}
.login-btn{position:absolute;left:975px;top:20px;width:205px;height:37px;background:var(--blue);color:var(--white);font-size:12.5px;font-weight:600;display:flex;align-items:center;justify-content:center}

/* hero */
.hero{position:absolute;top:77px;left:0;width:1200px;height:590px;background:var(--navy)}
.hero-media{position:absolute;left:634px;top:0;width:566px;height:590px;background:linear-gradient(135deg,#cfd6dc,#8ea6b7 45%,#4a3a2e);clip-path:polygon(86px 0,100% 0,100% 100%,0 100%,0 86px)}
.hero-title{position:absolute;left:110px;top:73px;width:480px;font-size:46px;line-height:53px;font-weight:700;color:var(--white)}
.hero-text{position:absolute;left:110px;top:307px;width:380px;font-size:14px;line-height:22px;color:var(--white)}
.btn-white{position:absolute;left:110px;top:399px;width:105px;height:50px;background:var(--white);color:var(--navy);font-size:12px;font-weight:700;display:flex;align-items:center;justify-content:center}
.hero-arrows{position:absolute;left:108px;top:509px;display:flex;gap:16px}

/* search */
.search-band{position:absolute;top:667px;left:0;width:1200px;height:289px;background:var(--grey)}
.search-icons{position:absolute;left:110px;top:74px;display:flex}
.search-icons span{width:36px;height:36px;border-radius:50%;background:var(--white);display:flex;align-items:center;justify-content:center;margin-right:-4px;box-shadow:0 0 0 2px var(--grey)}
.search-label{position:absolute;left:194px;top:82px;font-size:17px;color:var(--ink)}
.search-label b{font-weight:700}
.adv-search{position:absolute;right:111px;top:85px;font-size:12px;font-weight:600;color:var(--ink);display:flex;gap:5px;align-items:center}
.search-input{position:absolute;left:110px;top:132px;width:817px;height:51px;background:var(--white);border:1px solid var(--line);font-size:13px;color:var(--muted);padding-left:16px;display:flex;align-items:center}
.find-btn{position:absolute;left:934px;top:132px;width:155px;height:51px;background:var(--gold);color:var(--white);font-size:12.5px;font-weight:700;display:flex;align-items:center;justify-content:center;gap:10px}
.search-note{position:absolute;left:110px;top:203px;font-size:9.5px;color:var(--ink)}

/* features */
.eyebrow{position:absolute;display:flex;align-items:center;font-size:11px;font-weight:600;color:var(--navy);text-transform:uppercase}
.eyebrow::before{content:"";width:37px;height:2px;background:var(--navy);margin-right:14px}
.feature-title{position:absolute;font-size:32px;line-height:42px;font-weight:700;color:var(--ink)}
.feature-text{position:absolute;font-size:13.5px;line-height:23.5px;color:var(--text)}
.btn-blue{position:absolute;width:100px;height:50px;background:var(--blue);color:var(--white);font-size:12px;font-weight:700;display:flex;align-items:center;justify-content:center}
.feature-media{position:absolute;left:110px;top:1515px;width:331px;height:423px;background:linear-gradient(160deg,#a9a296,#d9cfc3 50%,#6b5847);clip-path:polygon(40px 0,100% 0,100% 100%,0 100%,0 40px)}

/* news */
.news-band{position:absolute;top:2040px;left:0;width:1200px;height:627px;background:var(--grey)}
.news-heading{position:absolute;left:110px;top:99px;font-size:30px;font-weight:700;color:var(--ink)}
.news-nav{position:absolute;right:111px;top:108px;display:flex;align-items:center;font-size:12px;color:var(--ink)}
.news-nav .sep{width:1px;height:14px;background:var(--line);margin:0 14px}
.news-card{position:absolute;top:168px;width:312px;height:316px;background:var(--white)}
.news-icon{position:absolute;left:27px;top:26px;width:40px;height:40px;border-radius:50%;background:var(--gold);display:flex;align-items:center;justify-content:center}
.news-title{position:absolute;left:27px;bottom:74px;width:275px;font-size:29px;line-height:42px;font-weight:700;color:var(--gold);text-decoration:underline;text-underline-offset:4px}
.news-date{position:absolute;left:27px;top:274px;font-size:12px;color:var(--ink)}

/* footer */
.site-footer{position:absolute;top:2667px;left:0;width:1200px;height:373px;border-top:1px solid var(--line)}
.map{position:absolute;left:767px;top:2626px;width:433px;height:342px;background:linear-gradient(135deg,#e6e8e3,#d4dcc9 60%,#a9c9e3);clip-path:polygon(0 0,100% 0,100% 100%,52px 100%,0 290px)}
.address-card{position:absolute;left:793px;top:2655px;width:256px;height:112px;background:var(--white);padding:26px 22px}
.address-card h4{font-size:9.5px;font-weight:500;color:var(--muted);text-transform:uppercase;margin-bottom:12px}
.address-card p{font-size:13px;line-height:20px;font-weight:500;color:var(--ink);white-space:nowrap}
.foot-col{position:absolute;top:2764px}
.foot-col h4{font-size:9.5px;font-weight:700;color:var(--ink);text-transform:uppercase;margin-bottom:18px}
.foot-col li{list-style:none;font-size:12px;font-weight:600;color:var(--ink);line-height:28px}
.foot-col.plain li{font-weight:500}
.foot-bottom{position:absolute;top:2995px;left:110px;width:980px;display:flex;justify-content:space-between;font-size:12px;font-weight:500;color:var(--ink)}
</style>
</head>
<body>

<header class="site-header">
  <div class="brand">BMPGT</div>
  <nav class="main-nav">
    <svg class="search-ico" width="12" height="12" viewBox="0 0 12 12"><circle cx="5" cy="5" r="3.8" fill="none" stroke="#111" stroke-width="1.8"/><path d="M8 8l3 3" stroke="#111" stroke-width="1.8"/></svg>
    <span class="sep"></span>
    <a>Public<span class="caret">▾</span></a>
    <a>Physicians<span class="caret">▾</span></a>
    <a>About<span class="caret">▾</span></a>
    <a>News<span class="caret">▾</span></a>
    <a>Contact</a>
  </nav>
  <a class="login-btn">Members &amp; Applicants Login</a>
</header>

<section class="hero">
  <div class="hero-media" role="img" aria-label="Physician in a light blue shirt holding a tablet while talking with a patient"></div>
  <h1 class="hero-title">Quality Assurance: Improvement Through Continuing Medical Education</h1>
  <p class="hero-text">Lorem Ipsum is simply dummy text of the printing and typesetting industry. Lorem Ipsum has been the industry's standard dummy text ever since the 1500s.</p>
  <a class="btn-white">Learn More</a>
  <div class="hero-arrows">
    <svg width="16" height="12" viewBox="0 0 16 12"><path d="M15 6H2M6 1L1 6l5 5" fill="none" stroke="#c9cfdb" stroke-width="1.6"/></svg>
    <svg width="16" height="12" viewBox="0 0 16 12"><path d="M1 6h13M10 1l5 5-5 5" fill="none" stroke="#fff" stroke-width="1.6"/></svg>
  </div>
</section>

<section class="search-band">
  <div class="search-icons">
    <span><svg width="11" height="11" viewBox="0 0 12 12"><circle cx="5" cy="5" r="3.8" fill="none" stroke="#111" stroke-width="1.8"/><path d="M8 8l3 3" stroke="#111" stroke-width="1.8"/></svg></span>
    <span><svg width="13" height="11" viewBox="0 0 14 12"><circle cx="5" cy="3.5" r="2.5" fill="none" stroke="#111" stroke-width="1.4"/><circle cx="10" cy="3.5" r="2" fill="none" stroke="#111" stroke-width="1.4"/><path d="M1 11c0-3 2-4.5 4-4.5s4 1.5 4 4.5M9 7c2 0 4 1 4 4" fill="none" stroke="#111" stroke-width="1.4"/></svg></span>
  </div>
  <div class="search-label">Physician <b>Search</b></div>
  <div class="adv-search"><svg width="11" height="11" viewBox="0 0 12 12"><path d="M1 1h10L7 6v5L5 10V6z" fill="none" stroke="#111" stroke-width="1.4"/></svg>Advanced Search</div>
  <div class="search-input">Type Physician's Last Name...</div>
  <a class="find-btn"><svg width="11" height="11" viewBox="0 0 12 12"><circle cx="5" cy="5" r="3.8" fill="none" stroke="#fff" stroke-width="1.8"/><path d="M8 8l3 3" stroke="#fff" stroke-width="1.8"/></svg>Find Physician</a>
  <p class="search-note">* This is a database of registered Greyhaven and Tollmere Doctors.</p>
</section>

<section class="features">
  <div class="eyebrow" style="left:110px;top:1057px">Physicians Applicants</div>
  <h2 class="feature-title" style="left:110px;top:1091px;width:420px">Interested in Practising Medicine in Greyhaven and Tollmere?</h2>
  <p class="feature-text" style="left:110px;top:1238px;width:400px">Lorem Ipsum is simply dummy text of the printing and typesetting industry. Lorem Ipsum has been the industry's standard dummy text ever since the 1500s, when an unknown printer took a galley of type and scrambled it...</p>
  <a class="btn-blue" style="left:110px;top:1359px">Learn More</a>

  <div class="eyebrow" style="left:676px;top:1057px">Practising Physicians</div>
  <h2 class="feature-title" style="left:676px;top:1093px;width:330px">Assuring Quality of Your Practice</h2>
  <p class="feature-text" style="left:676px;top:1199px;width:420px">Lorem Ipsum is simply dummy text of the printing and typesetting industry. Lorem Ipsum has been the industry's standard dummy text ever since the 1500s, when an unknown printer took a galley of type and scrambled it. When an unknown printer took a galley of type and scrambled it. When an unknown printer took a galley of type and scrambled it.</p>
  <a class="btn-blue" style="left:676px;top:1359px">Learn More</a>

  <div class="feature-media" role="img" aria-label="Hands signing a document on a clipboard with a pen"></div>

  <div class="eyebrow" style="left:681px;top:1551px">Complaints and Discipline</div>
  <h2 class="feature-title" style="left:681px;top:1586px;width:360px">Concerned About Medical Care that a Doctor has Provided?</h2>
  <p class="feature-text" style="left:681px;top:1733px;width:400px">Lorem Ipsum is simply dummy text of the printing and typesetting industry. Lorem Ipsum has been the industry's standard dummy text ever since the 1500s, when an unknown printer took a galley of type and scrambled it.</p>
  <a class="btn-blue" style="left:681px;top:1854px">Learn More</a>
</section>

<section class="news-band">
  <h2 class="news-heading">Most Recent News</h2>
  <div class="news-nav">View all news<span class="sep"></span>
    <svg width="16" height="12" viewBox="0 0 16 12"><path d="M15 6H2M6 1L1 6l5 5" fill="none" stroke="#111" stroke-width="1.6"/></svg>
    <svg width="16" height="12" viewBox="0 0 16 12" style="margin-left:12px"><path d="M1 6h13M10 1l5 5-5 5" fill="none" stroke="#111" stroke-width="1.6"/></svg>
  </div>
  <article class="news-card" style="left:110px">
    <span class="news-icon"><svg width="14" height="16" viewBox="0 0 14 16"><path d="M2 1h7l4 4v10H2z" fill="#fff"/><path d="M5 8h5M5 11h5" stroke="#7a4a12" stroke-width="1.2"/></svg></span>
    <h3 class="news-title">2019 Council<br>Election Results</h3>
    <p class="news-date">Posted on 12/2/2020</p>
  </article>
  <article class="news-card" style="left:444px">
    <span class="news-icon"><svg width="14" height="16" viewBox="0 0 14 16"><path d="M2 1h7l4 4v10H2z" fill="#fff"/><path d="M5 8h5M5 11h5" stroke="#7a4a12" stroke-width="1.2"/></svg></span>
    <h3 class="news-title">Indigenous<br>Physician Survey</h3>
    <p class="news-date">Posted on 12/2/2019</p>
  </article>
  <article class="news-card" style="left:777px">
    <span class="news-icon"><svg width="14" height="16" viewBox="0 0 14 16"><path d="M2 1h7l4 4v10H2z" fill="#fff"/><path d="M5 8h5M5 11h5" stroke="#7a4a12" stroke-width="1.2"/></svg></span>
    <h3 class="news-title">2019 Council<br>Elections -<br>Voting Reminder</h3>
    <p class="news-date">Posted on 12/2/2019</p>
  </article>
</section>

<footer class="site-footer"></footer>
<div class="map" role="img" aria-label="Street map showing the Board's office location"></div>
<div class="address-card">
  <h4>Address</h4>
  <p>48 Harbour Lane Suite B200,<br>Greyhaven, GT X0X 1A1</p>
</div>
<div class="foot-col" style="left:110px">
  <h4>Important Information</h4>
  <ul><li>Personal Health Information Act</li><li>Medical Practice Act and Regulations</li><li>Regional Medical Peer Review</li><li>Quality Assurance</li></ul>
</div>
<div class="foot-col plain" style="left:431px">
  <h4>Phone &amp; Fax</h4>
  <ul><li>(555) 014-2288</li><li>(555) 014-2290</li></ul>
</div>
<div class="foot-col plain" style="left:598px">
  <h4>Email</h4>
  <ul><li>info@bmpgt-site.ca</li></ul>
</div>
<div class="foot-bottom">
  <span>Terms &amp; Conditions · Media · Jobs · Disclaimer &amp; Privacy Policy</span>
  <span>All Rights Reserved, 2020 © BMPGT</span>
</div>

</body>
</html>
```